Logo and label lay out for Silver Moss wines

Wine Bottle label for single vineyard on The Mornington Peninsula, Victoria, Australia
Name of Vineyard is “Silver Moss”
(A silver Moss is a common biting ant found in the vineyard.)
The name and vintage of each of the four varieties of wine will need to be included on the label.
We want an instantly recognisable image on the label along with the name Silver Moss.

Target Market(s)

Quality wine for cafes, restaurants and individual’s wine collection

Industry/Entity Type

Vineyard

Logo Text

Silver Moss

Logo styles of interest
Emblem Logo
Abstract Logo
Colors

Designer to choose colors to be used in the design.

Requirements
Must have
• Simple yet stylish image, instantly recognisable .
Nice to have
• Possibly a stylistic image of an ant
Should not have
• Not an overly detailed image.

```html
<!DOCTYPE html>
<html lang="en">
<head>
<meta charset="utf-8">
<title>Silver Moss – Wine Labels</title>
<link rel="stylesheet" href="https://fonts.googleapis.com/css2?family=Jost:wght@300;400&display=swap">
<style>
  :root {
    --page-bg: #ffffff;
    --label-dark: #111111;
    --label-light: #efeedd;
    --mark-dark: #8a8a8a;
    --mark-gold: #b9a85a;
    --vintage-dark: #9a9a9a;
    --vintage-light: #4a4a4a;
    --variety-red: #a11a22;
    --variety-dark: #3c3c3c;
    --emblem-dark: #8a8a8a;
    --emblem-light: #2a2a2a;
  }
  * { margin: 0; padding: 0; box-sizing: border-box; }
  html, body {
    width: 877px;
    height: 1200px;
    overflow: hidden;
    background: var(--page-bg);
  }
  .label-set {
    width: 877px;
    height: 1200px;
    display: flex;
    justify-content: center;
    align-items: center;
    gap: 40px;
  }
  .label {
    width: 390px;
    height: 510px;
    display: flex;
    flex-direction: column;
    align-items: center;
    font-family: 'Jost', sans-serif;
  }
  .label--red { background: var(--label-dark); }
  .label--white { background: var(--label-light); }

  .brand {
    margin-top: 160px;
    display: flex;
    flex-direction: column;
    align-items: center;
  }
  .brand__emblem {
    width: 26px;
    height: 26px;
    border-radius: 50%;
    margin-bottom: 22px;
  }
  .label--red .brand__emblem { background: var(--emblem-dark); }
  .label--white .brand__emblem { background: var(--emblem-light); }

  .brand__name {
    font-weight: 400;
    font-size: 32px;
    line-height: 1.15;
    letter-spacing: 0.06em;
    text-align: center;
    text-transform: uppercase;
  }
  .label--red .brand__name { color: var(--mark-dark); }
  .label--white .brand__name { color: var(--mark-gold); }

  .wine-details {
    margin-top: auto;
    margin-bottom: 60px;
    text-align: center;
  }
  .wine-details__vintage {
    font-weight: 300;
    font-style: italic;
    font-size: 12px;
    letter-spacing: 0.12em;
    margin-bottom: 8px;
  }
  .label--red .wine-details__vintage { color: var(--vintage-dark); }
  .label--white .wine-details__vintage { color: var(--vintage-light); }

  .wine-details__variety {
    font-weight: 300;
    font-size: 15px;
    letter-spacing: 0.16em;
    text-transform: uppercase;
  }
  .label--red .wine-details__variety { color: var(--variety-red); }
  .label--white .wine-details__variety { color: var(--variety-dark); }
</style>
</head>
<body>
  <main class="label-set">
    <section class="label label--red">
      <div class="brand">
        <span class="brand__emblem"></span>
        <h1 class="brand__name">Silver<br>Moss</h1>
      </div>
      <div class="wine-details">
        <p class="wine-details__vintage">2017</p>
        <p class="wine-details__variety">Cabernet Sauvignon</p>
      </div>
    </section>
    <section class="label label--white">
      <div class="brand">
        <span class="brand__emblem"></span>
        <h1 class="brand__name">Silver<br>Moss</h1>
      </div>
      <div class="wine-details">
        <p class="wine-details__vintage">2017</p>
        <p class="wine-details__variety">Chardonnay</p>
      </div>
    </section>
  </main>
</body>
</html>
```